Water Damage? Call Us!!

We are an established water damage mitigation company opening a storm chasing division. We will need the flyer to express urgency to call for water damage structural drying and demolition. I have attached our logo in various formats.

Check out our website for some ideas of what we do. www.parklinerestoration.com

Include:

Parkline Restoration, LLC
Office@ParklineRestoration.com
www.parklinerestoration.com
877-HELP-NOW
877-435-7669

I don't want to have our locations on there.

Target Market(s)

When someone has water damage to their home or business, we remove the wet material and then use fans and dehumidifiers to remove the moisture from the structure. We are like a Kelvora, but better. Lol

Colors

Designer to choose colors to be used in the design.

Requirements
Must have
• I have included various certification logos to use.
• Water damage must be the main focal point.
• We need to call them to action by calling us to dry their property. We will be dropping these flyers off in damaged areas.
• Trained in Drying Science by the NBRTA
• We handle Residential, Commercial, Hotels, Multi-Family.
• We specialize in Insurance Claims.
• We can bill your insurance company directly.
• Our Services include:
• Water Extraction/Muck Out
• Deconstruction of Damaged Materials
• Structural Drying
• Anti-Microbial Application
• Roofing
Nice to have
• It would be nice to have some thermal images of wet areas
Should not have
• Not looking for a fun flyer. These potential clients have suffered from devastation and we are looking to help them by getting their home or business back to normal.

```html
<!DOCTYPE html>
<html lang="en">
<head>
<meta charset="utf-8">
<title>Parkline Restoration – Water Damage Flyer</title>
<link rel="stylesheet" href="https://fonts.googleapis.com/css2?family=Exo+2:ital,wght@0,700;0,800;1,800;1,900&family=Catamaran:wght@400;600;700&display=swap">
<style>
:root{
  --stage:#3b3b3c;
  --paper:#ffffff;
  --sky:#27a0de;
  --navy:#2b3a9a;
  --ink:#1d1d1f;
  --badge-grey:#9aa3ab;
}
*{box-sizing:border-box;margin:0;padding:0}
html,body{width:1200px;height:822px;overflow:hidden;background:var(--stage)}
body{position:relative;font-family:"Catamaran",sans-serif;color:var(--ink)}
.page{position:absolute;top:74px;width:498px;height:644px;background:linear-gradient(90deg,#e7e8ea 0%,#fff 35%,#fff 100%);overflow:hidden}
.page--front{left:95px}
.page--back{left:607px}
.shapes{position:absolute;left:0;top:0}
.bottom-band{position:absolute;left:0;bottom:0;width:100%;height:16px;background:var(--sky)}

/* front */
.brand{position:absolute;left:232px;top:336px;display:flex;align-items:center;gap:10px}
.brand__dot{width:34px;height:34px;border-radius:50%;background:var(--sky)}
.brand__name{font-family:"Exo 2",sans-serif;font-weight:800;font-size:31px;line-height:32px;color:var(--navy);letter-spacing:.5px}
.accent-bar{position:absolute;left:189px;top:418px;width:309px;height:8px;background:var(--sky);clip-path:polygon(8px 0,100% 0,100% 100%,0 100%)}
.headline{position:absolute;left:0;width:100%;top:440px;text-align:center;font-family:"Exo 2",sans-serif;font-style:italic;font-weight:900;font-size:28.5px;line-height:30px;color:var(--sky);letter-spacing:.2px}
.why-tab{position:absolute;left:0;top:516px;width:138px;height:22px;background:var(--sky);clip-path:polygon(0 0,116px 0,100% 100%,0 100%);color:#fff;font-weight:700;font-size:12.5px;padding:3px 0 0 33px}
.checks{position:absolute;list-style:none;font-size:9.6px;font-weight:600;line-height:11.7px}
.checks li{position:relative;padding-left:15px}
.checks li::before{content:"";position:absolute;left:1px;top:2px;width:6px;height:3.5px;border-left:2px solid var(--sky);border-bottom:2px solid var(--sky);transform:rotate(-45deg)}
.checks--left{left:32px;top:551px}
.checks--right{left:250px;top:539px}

/* back */
.intro{position:absolute;left:0;top:0;width:100%;padding:19px 20px 0;color:#fff;text-align:center;font-size:9.4px;line-height:11.7px}
.service{position:absolute;left:23px;width:292px}
.service__title{font-weight:700;font-size:13.2px;color:var(--sky);margin-bottom:5px;letter-spacing:.1px}
.service__body{font-size:7.9px;line-height:9.7px;text-align:justify}
.service--demo{top:160px}
.service--gc{top:257px}
.service--docs{top:355px}
.service-photo{position:absolute;left:333px;width:143px;border:2px solid var(--navy);border-radius:6px}
.service-photo--fans{top:161px;height:86px;background:linear-gradient(180deg,#7fa08a,#2d83c7 60%,#2f6fb3)}
.service-photo--house{top:252px;height:86px;background:linear-gradient(180deg,#6aa6e0,#a9c6ea 45%,#c9c3b3 75%,#9a9a86)}
.service-photo--drone{top:343px;height:87px;background:linear-gradient(180deg,#7e8fa5,#c9a46a 55%,#f0c060 70%,#5b4a38)}
.cta{position:absolute;left:29px;top:458px;width:440px;height:69px;border-radius:35px;background:var(--sky);color:#fff;text-align:center}
.cta__line{display:block;font-weight:700;font-size:32px;line-height:1;padding-top:12px;letter-spacing:-.3px}
.cta__phone{display:block;font-weight:700;font-size:16.5px;line-height:1;margin-top:4px}
.badges{position:absolute;left:40px;top:542px;width:430px;height:76px;display:flex;justify-content:space-between;align-items:center}
.badge{flex:none}
.badge--commercial{width:62px;height:44px;border-radius:4px;background:#c9a24a}
.badge--moisture{width:58px;height:58px;border-radius:50%;background:#2f8a4a}
.badge--exterior{width:46px;height:62px;background:#b45a2a}
.badge--cpi{width:58px;height:58px;border-radius:50%;background:#6b6b6b}
.badge--infrared{width:54px;height:54px;border-radius:50%;background:var(--badge-grey)}
.badge--roof{width:76px;height:36px;background:#8a5a3a}
</style>
</head>
<body>

<section class="page page--front">
  <svg class="shapes" width="498" height="644" viewBox="0 0 498 644">
    <defs>
      <linearGradient id="pipeTone" x1="0" y1="0" x2="1" y2="1">
        <stop offset="0" stop-color="#dfe3e7"/>
        <stop offset=".55" stop-color="#f4f5f6"/>
        <stop offset="1" stop-color="#b9bfc6"/>
      </linearGradient>
    </defs>
    <path role="img" aria-label="Photo of a hand tightening a wrench on a leaking white sink drain pipe with water spraying" d="M0 0H482C470 200 300 320 0 338Z" fill="url(#pipeTone)"/>
    <path d="M0 338C300 320 470 200 482 0H498V12C485 250 320 365 0 352Z" fill="var(--sky)"/>
    <path d="M0 352C320 365 485 250 498 12V28C478 270 320 375 0 360Z" fill="#ffffff"/>
    <path d="M90 362C330 360 478 280 498 60V74C470 300 300 372 90 362Z" fill="var(--navy)"/>
  </svg>

  <div class="brand"><span class="brand__dot"></span><span class="brand__name">PARKLINE<br>RESTORATION</span></div>
  <div class="accent-bar"></div>

  <h1 class="headline">WATER DAMAGE STRUCTURAL<br>DRYING AND DEMOLITION</h1>

  <div class="why-tab">Why Us?</div>
  <ul class="checks checks--left">
    <li>Trained in Structural Drying Science</li>
    <li>Trained Insurance Adjusters</li>
    <li>Trained in Building Sciences</li>
    <li>Can bill your insurance company directly</li>
    <li>Residential</li>
  </ul>
  <ul class="checks checks--right">
    <li>Commercial</li>
    <li>3 decades of general contracting experience</li>
    <li>Able to handle your complete project turnkey</li>
    <li>Detailed Documentation of your property loss</li>
    <li>Multi-Family</li>
    <li>Hotel/Motel</li>
  </ul>

  <div class="bottom-band"></div>
</section>

<section class="page page--back">
  <svg class="shapes" width="498" height="644" viewBox="0 0 498 644">
    <path d="M0 0H498V118C330 132 170 132 0 112Z" fill="var(--sky)"/>
    <path d="M0 112C170 132 330 132 498 118V124C330 140 170 140 0 118Z" fill="var(--navy)"/>
  </svg>

  <p class="intro">Parkline Restoration is uniquely positioned to be one of the leading restoration companies in the state. The owners, Dana Whitfield &amp; Marcus Leland are certified in Structural Drying Science by the NBRTA. In addition, Dana &amp; Marcus are licensed insurance adjusters who have handled thousands of claims from the side of the insurance carriers. They take the knowledge they have learned from decades of handling insurance claims and are able to make your claims experience a breeze. The trained Staff at Parkline Restoration will meet your insurance adjuster on site and provide detailed documentation of your property and the loss. Insurance adjusters LOVE to work with Parkline Restoration because when they adjust a claim where Parkline Restoration is the contractor, they know their job just got easier.</p>

  <article class="service service--demo">
    <h2 class="service__title">DEMOLITION &amp; STRUCTURAL DRYING</h2>
    <p class="service__body">Demolition, or removing the wet material, is often the best course of action after a water loss. The main factors include both the length of time the building materials were wet and the water source. A Category 1 water is when there was a clean water source such as a sink overflow and the damage has just occurred. In a Category 1 situation, then the material can sometimes be dried in place without demolition.</p>
  </article>
  <div class="service-photo service-photo--fans" role="img" aria-label="Photo of rows of blue air movers staged outside a building"></div>

  <article class="service service--gc">
    <h2 class="service__title">GENERAL CONTRACTING</h2>
    <p class="service__body">Parkline Restoration can handle every aspect of your project. We provide General Contracting Services so no need to look around to find multiple companies to handle the different aspects of your project. Parkline Restoration can replace your roof, replace your drywall and give it the perfect paint finish or even replace your fencing. To save on your energy bills, it may be time for Parkline Restoration to blow new insulation in your attic.</p>
  </article>
  <div class="service-photo service-photo--house" role="img" aria-label="Photo of a stucco house with a tile roof under a blue sky"></div>

  <article class="service service--docs">
    <h2 class="service__title">PROPERTY DOCUMENTATION</h2>
    <p class="service__body">Proper documentation is probably the most important thing at the beginning of a project. If a property loss is documented in detail, making changes/updates to the scope of work can be seamless. Parkline Restoration has perfected property documentation by utilizing the latest technology. The Lumaspace Camera and Software Technology allows us to scan the property in complete 360 view.</p>
  </article>
  <div class="service-photo service-photo--drone" role="img" aria-label="Photo of a drone flying over a property at sunset"></div>

  <div class="cta">
    <span class="cta__line">GIVE US A CALL TODAY!</span>
    <span class="cta__phone">1 (877) HELP-NOW (877-435-7669)</span>
  </div>

  <div class="badges" aria-label="Certifications">
    <span class="badge badge--commercial"></span>
    <span class="badge badge--moisture"></span>
    <span class="badge badge--exterior"></span>
    <span class="badge badge--cpi"></span>
    <span class="badge badge--infrared"></span>
    <span class="badge badge--roof"></span>
  </div>

  <div class="bottom-band"></div>
</section>

</body>
</html>
```